Redo a PPT pres. - Real Estate in Brazil - Socially equitable investments in Social Housing

We need to redo the presentation attached. It is an institutional presentation to attract local and foreign investors to invest in Brazilian Social Housing Projects structured by our company "RTV".
A middle class of 100 million, a housing deficit of 9M, a strong political will & positive income generation trends constitute grounds for a significant demand in social housing.
This make a perfect scheme for investors to invest in Brazilian Social Housing.
"RTV", is a consulting "boutique" focused in Brazilian real estate, specialized in structuring, analyzing and originating Brazilian social housing projects.
RTV is part of the group RTP. RTP is structured to create value through each step of the residential real estate business - structuring, financing, sales, marketing and technology.
We would like to see designs that use mainly the color blue. The final design should communicate financial safety and professionalism. In order to reach our needs, the designer will need to have basic understanding of finance and investment in order to highlight the most important information.
The idea is to receive back the PPT with each page redesigned and an homogeneous identity.
To all designers,
Target Market(s)
Institutional Investors and wealthy individuals
Industry/Entity Type
Residential
Look and feel
Each slider illustrates characteristics of the customer's brand and the style your logo design should communicate.

```html
<!DOCTYPE html>
<html lang="en">
<head>
<meta charset="utf-8">
<title>RTP Focus – Slide Redesign</title>
<link href="https://fonts.googleapis.com/css2?family=Montserrat:wght@400;600;700;800&family=Open+Sans:wght@400;600;700&display=swap" rel="stylesheet">
<style>
:root{
  --stage:#000;
  --white:#fff;
  --navy:#1b2a5c;
  --navy-deep:#141f45;
  --green:#74c043;
  --band-green:#3c8a3a;
  --ink:#1f2330;
  --body:#383d4c;
  --rule:#c9cfdb;
  --header-bg:#eceef4;
  --old-title:#2a3d6e;
  --old-accent:#1f3f8a;
}
*{box-sizing:border-box;margin:0;padding:0}
html,body{width:1200px;height:837px;overflow:hidden;background:var(--stage)}
body{position:relative;font-family:"Open Sans",Arial,sans-serif}

.label{position:absolute;color:var(--white);font-family:"Montserrat",Arial,sans-serif;font-weight:800;font-size:25px;text-align:center;letter-spacing:.5px}
.label-old{left:122px;top:74px;width:300px}
.label-new{left:765px;top:74px;width:300px}
.label-sub{position:absolute;left:765px;top:108px;width:300px;text-align:center;color:var(--green);font-family:"Montserrat",Arial,sans-serif;font-weight:700;font-size:15px}

/* old slide */
.old-slide{position:absolute;left:85px;top:316px;width:374px;height:293px;background:var(--white);padding:10px 14px 8px 20px}
.old-title{font-weight:700;font-size:12px;color:var(--old-title);border-bottom:1px solid var(--rule);padding-bottom:2px}
.old-sub{font-weight:700;font-size:9.6px;line-height:1.35;color:var(--old-title);margin-top:4px;width:340px}
.old-cols{display:flex;gap:14px;margin-top:9px}
.old-col{flex:1}
.old-head{display:flex;align-items:center;gap:3px;font-weight:700;font-size:6px;color:var(--old-title);border-bottom:1px solid var(--rule);padding-bottom:1px;margin-bottom:3px}
.old-head::before{content:"";width:5px;height:5px;border-radius:50%;background:var(--old-accent)}
.old-list{list-style:disc;padding-left:10px;font-size:3.7px;line-height:1.4;color:var(--ink)}
.old-list li.strong{font-weight:700}
.old-wide{margin-top:9px}
.old-page{position:absolute;right:12px;bottom:7px;font-size:5px;color:var(--body)}

/* new pages */
.page{position:absolute;left:707px;width:390px;background:var(--white);display:flex}
.page-1{top:169px;height:281px}
.page-2{top:454px;height:306px}
.side{position:relative;width:106px;height:100%;overflow:hidden}
.side-photo{position:absolute;inset:0;background:linear-gradient(180deg,#2b4892 0%,#3a5fae 40%,#28407f 75%,#1d2f63 100%)}
.ribbon{position:absolute;left:20px;top:0;width:60px;height:58px}
.ribbon-name{position:absolute;left:20px;top:18px;width:60px;text-align:center;color:var(--white);font-family:"Montserrat",Arial,sans-serif;font-weight:700;font-size:10px}
.badge{position:absolute;left:8px;top:30px;width:90px;height:90px;border-radius:50%;background:rgba(255,255,255,.18);border:2px solid rgba(255,255,255,.75);display:flex;align-items:center;justify-content:center;text-align:center;color:var(--white);font-size:6.4px;line-height:1.35;padding:14px}
.page-1 .badge{top:33px}
.page-2 .badge{top:64px}
.side-title{position:absolute;left:0;width:100%;text-align:center;color:var(--white);font-family:"Montserrat",Arial,sans-serif;font-weight:800;font-size:9.5px;letter-spacing:.4px}
.page-1 .side-title{top:188px}
.page-2 .side-title{top:205px}
.side-cont{position:absolute;left:0;top:219px;width:100%;text-align:center;color:var(--green);font-family:"Montserrat",Arial,sans-serif;font-weight:700;font-size:6.5px}
.side-band{position:absolute;left:0;width:100%;height:26px;background:var(--band-green);color:var(--white);font-size:4.6px;line-height:1.35;font-weight:700;text-align:center;padding:4px 6px}
.page-1 .side-band{top:245px}
.page-2 .side-band{top:266px}

.content{flex:1;padding:12px 14px 0 12px;position:relative}
.sec-head{background:var(--header-bg);border-left:3px solid var(--navy);font-family:"Montserrat",Arial,sans-serif;font-weight:800;font-size:6px;color:var(--navy);padding:3px 5px;margin-bottom:4px}
.new-list{list-style:disc;padding-left:10px;font-size:4.6px;line-height:1.5;color:var(--body);margin-bottom:10px}
.new-list li.strong{font-weight:700;color:var(--ink)}
.pager{position:absolute;right:12px;bottom:9px;display:flex;align-items:center;gap:3px;font-size:5px;font-weight:700;color:var(--navy)}
</style>
</head>
<body>

<div class="label label-old">OLD SLIDE</div>
<div class="label label-new">NEW SLIDE</div>
<div class="label-sub">(SPLIT TO 2 PAGES)</div>

<section class="old-slide">
  <h1 class="old-title">RTP Focus</h1>
  <p class="old-sub">A focus on Social Housing and Brokerage supported by strong technology and an online marketing platform</p>
  <div class="old-cols">
    <div class="old-col">
      <h2 class="old-head">The Social Housing</h2>
      <ul class="old-list">
        <li>Concentrated in the hand of the small/mid-size developers while listed developers are mainly focused on the mid to high-income segment.</li>
        <li>Small/mid-size developers are not receiving the attention they need from the investment bank community and are not under the radar of potential investors.</li>
        <li>Bottlenecks of social housing include (i) tight construction costs difficult to be managed by large companies and (ii) inefficient mortgage application process (Lar Federal).</li>
        <li class="strong">As a response, RTP is offering the services of RTVI (Mortgage application) and RTV (consulting).</li>
      </ul>
    </div>
    <div class="old-col">
      <h2 class="old-head">The Brokerage Market</h2>
      <ul class="old-list">
        <li>Real Estate brokers in Brazil lack training, support and, as a result, are considered unprofessional by potential customers.</li>
        <li>The massive private primary housing market in Brazil is controlled by a duopoly, representing more than 40% of the market.</li>
        <li>Various developers have expressed their frustration with the lack of commercialization options.</li>
        <li class="strong">RTP created Keystone to offer Brazilian developers a third option by proposing a new kind of brokerage experience inspired by large brokers in Europe and the US.</li>
        <li class="strong">RTP also started working on Keystone concept, allowing developers to reach local real estate agencies.</li>
      </ul>
    </div>
  </div>
  <div class="old-wide">
    <h2 class="old-head">The Technology</h2>
    <ul class="old-list">
      <li>Technology is RTP's centerpiece to provide the real estate market with an efficient and successful Brokerage and Social Housing service.</li>
      <li>As an investment banker during more than 4 years in NYC, RTP saw the efficiency of the NLS technology in the USA and the necessity to have two brokers representing both parties in a real estate transaction.</li>
      <li>Realizing the lack of professionalism in the real estate brokerage industry (only one broker representing both parties, no technology tools, no partnership between real estate agencies), Nuvalor was acquired to better serve the real estate industry.</li>
      <li>With Nuvalor, RTP owns the first Brazilian real estate office management solution providing the 1st NLS system to Brazil. It manages the real estate data, trains the brokers and works on improving market liquidity by developing tools to allow shared commissions and partnerships between brokers.</li>
      <li>As a ground-breaking real estate portal, Casa Link will have real estate information updated in real-time thanks to the interconnection between Nuvalor clients, their websites and the capability to automatically publish listings on Casa Link.</li>
      <li class="strong">With Casa Link, Nuvalor will work directly with the real estate buyer. As the only platform between the real estate agency, the developer and the end customer, Nuvalor is building a truly unique offering.</li>
    </ul>
  </div>
  <span class="old-page">25</span>
</section>

<section class="page page-1">
  <div class="side">
    <div class="side-photo" role="img" aria-label="Blue-toned city skyline photograph"></div>
    <svg class="ribbon" viewBox="0 0 60 58" aria-hidden="true"><polygon points="0,0 60,0 60,58 30,48 0,58" fill="#141f45"/></svg>
    <div class="ribbon-name">RTV</div>
    <div class="badge">RTV, Part of An integrated Family of companies</div>
    <div class="side-title">RTP FOCUS</div>
    <div class="side-band">A focus on Social Housing and Brokerage supported by strong technology and an online marketing platform</div>
  </div>
  <div class="content">
    <h2 class="sec-head">THE ONLINE HOUSING</h2>
    <ul class="new-list">
      <li>Concentrated in the hand of the small/mid-size developers while listed developers are mainly focused on the mid to high-income segment.</li>
      <li>Small/mid-size developers are not receiving the attention they need from the investment bank community and are not under the radar of potential investors.</li>
      <li>Bottlenecks of social housing include (i) tight construction costs difficult to be managed by large companies and (ii) inefficient mortgage application process (Lar Federal).</li>
      <li class="strong">As a response, RTP is offering the services of RTVI (Mortgage application) and RTV (consulting).</li>
    </ul>
    <h2 class="sec-head">THE BROKERAGE MARKET</h2>
    <ul class="new-list">
      <li>Real Estate brokers in Brazil lack training, support and, as a result, are considered unprofessional by potential customers.</li>
      <li>The massive private primary housing market in Brazil is controlled by a duopoly, representing more than 40% of the market.</li>
      <li>Various developers have expressed their frustration with the lack of commercialization options.</li>
      <li class="strong">RTP created Keystone to offer Brazilian developers a third option by proposing a new kind of brokerage experience inspired by the large brokers in Europe and the US.</li>
      <li class="strong">RTP also started working on Keystone concept, allowing developers to reach local real estate agencies.</li>
    </ul>
    <div class="pager">
      <svg width="6" height="6" viewBox="0 0 6 6" aria-hidden="true"><path d="M4 1 L2 3 L4 5" stroke="#1b2a5c" fill="none" stroke-width="1"/></svg>
      <span>04</span>
      <svg width="6" height="6" viewBox="0 0 6 6" aria-hidden="true"><path d="M2 1 L4 3 L2 5" stroke="#1b2a5c" fill="none" stroke-width="1"/></svg>
    </div>
  </div>
</section>

<section class="page page-2">
  <div class="side">
    <div class="side-photo" role="img" aria-label="Blue-toned city skyline photograph"></div>
    <svg class="ribbon" viewBox="0 0 60 58" aria-hidden="true"><polygon points="0,0 60,0 60,58 30,48 0,58" fill="#141f45"/></svg>
    <div class="ribbon-name">RTV</div>
    <div class="badge">RTV, Part of An integrated Family of companies</div>
    <div class="side-title">RTP FOCUS</div>
    <div class="side-cont">(CONTINUE)</div>
    <div class="side-band">A focus on Social Housing and Brokerage supported by strong technology and an online marketing platform</div>
  </div>
  <div class="content">
    <h2 class="sec-head">THE TECHNOLOGY</h2>
    <ul class="new-list">
      <li>Technology is RTP's centerpiece to provide the real estate market with an efficient and successful Brokerage and Social Housing service.</li>
      <li>As an investment banker during more than 4 years in NYC, RTP saw the efficiency of the NLS technology in the USA and the necessity to have two brokers representing both parties in a real estate transaction.</li>
      <li>Realizing the lack of professionalism in the real estate brokerage industry (only one broker representing both parties, no technology tools, no partnership between real estate agencies), Nuvalor was acquired to better serve the real estate industry.</li>
      <li>With Nuvalor, RTP owns the first Brazilian real estate office management solution providing the 1st NLS system to Brazil. It manages the real estate data, trains the brokers and works on improving the real estate market liquidity by developing the tools to allow shared commissions and partnerships between brokers.</li>
      <li>As a ground-breaking real estate portal, Casa Link will have real estate information updated in real-time thanks to the interconnection between Nuvalor clients, their websites and the capability to automatically publish listings on Casa Link.</li>
      <li class="strong">With Casa Link, Nuvalor will work directly with the real estate buyer. As the only platform between the real estate agency, the developer and the end customer, Nuvalor is building a truly unique offering.</li>
    </ul>
    <div class="pager">
      <svg width="6" height="6" viewBox="0 0 6 6" aria-hidden="true"><path d="M4 1 L2 3 L4 5" stroke="#1b2a5c" fill="none" stroke-width="1"/></svg>
      <span>04</span>
      <svg width="6" height="6" viewBox="0 0 6 6" aria-hidden="true"><path d="M2 1 L4 3 L2 5" stroke="#1b2a5c" fill="none" stroke-width="1"/></svg>
    </div>
  </div>
</section>

</body>
</html>
```